Brindle Logistics Business Card Design

We are a trucking and warehousing company. We run freight in the US manly from the Pacific NW to TX and back up the the PNW. We also do warehousing where we store, move, and distribute freight. Looking for a clean and modern design of business card. We would like to look rich and elegant. Attached is our logo.

Industry/Entity Type

Trucking Company

Contact Information for Business Card

Looking for a clean and modern design of business card. We would like to look rich and elegant.

Font styles to use
Sans Serif

Colors

Designer to choose colors to be used in the design.

Requirements
Must have
• logo but it should not dominate the card
Should not have
• logo should not dominate the card

```html
<!DOCTYPE html>
<html lang="en">
<head>
<meta charset="utf-8">
<title>Brindle Logistics Business Card</title>
<link href="https://fonts.googleapis.com/css2?family=Michroma&family=Source+Sans+3:wght@400;600&display=swap" rel="stylesheet">
<style>
  :root {
    --stage: #8a8a8a;
    --brand-blue: #0072bb;
    --brand-orange: #f7941d;
    --paper: #ffffff;
    --ink: #3a3a3a;
  }
  html, body {
    margin: 0;
    width: 1200px;
    height: 802px;
    overflow: hidden;
    background: var(--stage);
  }
  .stage { position: relative; width: 1200px; height: 802px; }
  .card {
    position: absolute;
    top: 274px;
    width: 442px;
    height: 265px;
    box-shadow: 2px 3px 6px rgba(0,0,0,.45);
    overflow: hidden;
  }
  .card-front { left: 136px; background: var(--brand-blue); color: var(--paper); }
  .card-back { left: 624px; background: var(--paper); }

  .art-area {
    position: absolute; left: 0; top: 0; width: 160px; height: 265px;
  }
  .holder {
    position: absolute; right: 24px; top: 45px; text-align: right;
  }
  .holder-name {
    font-family: "Michroma", sans-serif; font-size: 12px; letter-spacing: .3px; margin: 0;
  }
  .holder-role {
    font-family: "Source Sans 3", sans-serif; font-size: 12px; margin: 1px 0 0;
  }
  .contact {
    position: absolute; right: 24px; top: 144px; margin: 0; padding: 0; list-style: none;
    font-family: "Source Sans 3", sans-serif; font-size: 12px; line-height: 16px; text-align: right;
  }
  .contact li { display: flex; justify-content: flex-end; align-items: center; gap: 4px; }
  .contact svg { width: 10px; height: 10px; fill: var(--paper); }
  .address {
    position: absolute; right: 26px; top: 211px; margin: 0;
    font-family: "Source Sans 3", sans-serif; font-size: 12px; line-height: 16px; text-align: right;
    font-style: normal;
  }

  .wordmark {
    position: absolute; left: 106px; top: 117px;
    display: flex; align-items: center; gap: 8px;
  }
  .wordmark-dot { width: 30px; height: 30px; border-radius: 50%; background: var(--brand-blue); flex: none; }
  .wordmark-name {
    font-family: "Source Sans 3", sans-serif; font-weight: 600; font-size: 16px;
    letter-spacing: .5px; color: var(--ink); margin: 0; white-space: nowrap;
  }
</style>
</head>
<body>
<main class="stage">
  <section class="card card-front">
    <svg class="art-area" viewBox="0 0 160 265" role="img" aria-label="Illustration area in orange and white tones">
      <defs>
        <linearGradient id="artTone" x1="0" y1="0" x2="1" y2="1">
          <stop offset="0" stop-color="#ffffff"/>
          <stop offset=".6" stop-color="#f7941d"/>
          <stop offset="1" stop-color="#f9b25c"/>
        </linearGradient>
      </defs>
      <rect x="0" y="0" width="160" height="265" fill="url(#artTone)"/>
    </svg>

    <div class="holder">
      <p class="holder-name">DANIEL HARTWELL</p>
      <p class="holder-role">Managing Director</p>
    </div>

    <ul class="contact">
      <li>044-123 456 789 <svg viewBox="0 0 10 10"><path d="M1 3 C1 1 9 1 9 3 L8 4 L6.5 3.2 V2.6 H3.5 V3.2 L2 4 Z M2.5 5 H7.5 L8.5 9 H1.5 Z"/></svg></li>
      <li>044-123 456 789 <svg viewBox="0 0 10 10"><path d="M2.5 0 H7.5 V10 H2.5 Z M3.5 1 V8 H6.5 V1 Z" fill-rule="evenodd"/></svg></li>
      <li>info@brindlefreight.com <svg viewBox="0 0 10 10"><path d="M0 2 H10 V8.5 H0 Z M1 3 L5 6 L9 3 Z" fill-rule="evenodd"/></svg></li>
      <li>www.brindlefreight.com <svg viewBox="0 0 10 10"><circle cx="5" cy="5" r="4.8"/></svg></li>
    </ul>
    <address class="address">12345, Address Goes Here<br>Country Name, 123456</address>
  </section>

  <section class="card card-back">
    <div class="wordmark">
      <span class="wordmark-dot"></span>
      <p class="wordmark-name">BRINDLE LOGISTICS, LLC</p>
    </div>
  </section>
</main>
</body>
</html>
```